New webpage design for development bureau

We are a development bureau in Denmark, and need a design for our webpage. We are called Tindral Development (Part of Tindral Brisk Skolary Group), and are going to aim for multiple markets: Web, Apps, Desktop applications, ect.

We already have a logo, see the uploaded file. We do not have any special demands, other than in have to be simple. A portfolio view should also be available, for future customers.

```html
<!DOCTYPE html>
<html lang="en">
<head>
<meta charset="utf-8">
<title>Tindral Development</title>
<link rel="stylesheet" href="https://fonts.googleapis.com/css2?family=Cabin:wght@400;500;600;700&family=Open+Sans:wght@400;600&display=swap">
<style>
:root{
  --ink:#222222;
  --topbar:#1f1f1f;
  --blue:#3ab6e8;
  --blue-dark:#2aa3d6;
  --nav-active:#2b2b2b;
  --orange:#f07f1b;
  --text:#333333;
  --white:#ffffff;
  --footer:#2a2a2a;
}
*{margin:0;padding:0;box-sizing:border-box}
html,body{width:826px;height:1200px;overflow:hidden;background:var(--white)}
body{position:relative;font-family:"Open Sans",Arial,sans-serif;color:var(--text)}
.abs{position:absolute}

/* top bar */
.top-bar{left:0;top:0;width:826px;height:30px;background:var(--topbar)}
.toll{right:81px;top:9px;font-size:9.5px;color:#ddd}
.toll b{color:#fff}

/* navigation */
.nav{left:0;top:30px;width:826px;height:38px;background:linear-gradient(#47c0ef,var(--blue-dark))}
.brand{left:83px;top:8px;font-family:"Cabin",sans-serif;font-weight:700;font-size:19px;color:var(--ink);letter-spacing:.5px}
.menu{left:0;top:0;height:38px}
.menu a{position:absolute;top:0;height:38px;line-height:38px;font-family:"Cabin",sans-serif;font-size:10px;color:#fff;text-decoration:none;white-space:nowrap}
.menu a.active{background:var(--nav-active);padding:0 10px}
.social{top:13px;height:13px;display:flex;gap:2px}
.social span{width:13px;height:13px;border-radius:50%;background:#fff;display:block}
.nav .social span:last-child{background:var(--ink)}

/* hero */
.hero{left:0;top:68px;width:826px;height:346px;background:linear-gradient(100deg,#2a2b2e 0%,#3a3630 40%,#6b5a45 62%,#c8c6c2 78%,#8a7658 100%)}
.hero-title{left:80px;top:196px;font-family:"Cabin",sans-serif;font-weight:400;font-size:24.5px;line-height:30px;color:#fff}
.btn-cta{left:82px;top:274px;width:123px;height:31px;background:var(--blue);color:#fff;font-family:"Cabin",sans-serif;font-size:13.5px;line-height:31px;text-align:center}
.learn{font-family:"Cabin",sans-serif;font-size:8.5px;color:var(--orange);display:flex;align-items:center;gap:4px;white-space:nowrap}
.learn i{display:inline-block;width:11px;height:8px;background:var(--orange);position:relative}
.learn i::after{content:"";position:absolute;left:3px;top:2px;border-left:5px solid #fff;border-top:2px solid transparent;border-bottom:2px solid transparent}
.dots{left:718px;top:386px;display:flex;gap:2px}
.dots span{width:7px;height:7px;border-radius:50%;background:#bbb}
.dots span:first-child{background:#fff}

/* section headings */
.section-title{font-family:"Cabin",sans-serif;font-weight:400;color:var(--blue);font-size:19px}
.rule{height:0;border-top:1px dotted #444}
.rule-bar{height:5px;background:#000}

/* services */
.svc{width:190px;text-align:center}
.svc h3{font-family:"Cabin",sans-serif;font-weight:400;font-size:13px;color:#444;margin-bottom:8px}
.svc p{font-size:8.5px;line-height:12.5px;color:var(--text)}
.svc .learn{justify-content:center;margin-top:15px}

/* lower columns */
.col-title{font-family:"Cabin",sans-serif;font-weight:600;font-size:12.5px;color:var(--blue)}
.about-text{font-size:8.5px;line-height:12.5px;color:var(--text)}
.tile{width:116px;height:104px;background:#555}
.tile .cap{position:absolute;left:0;bottom:0;width:116px;height:16px;background:#2b2b2b;color:#fff;font-size:7.5px;line-height:16px;padding-left:10px}
.tile .cap i{position:absolute;right:5px;top:4px;width:11px;height:8px;background:var(--orange)}
.tile .cap i::after{content:"";position:absolute;left:3px;top:2px;border-left:5px solid #fff;border-top:2px solid transparent;border-bottom:2px solid transparent}

/* footer */
.footer{left:0;top:1170px;width:826px;height:30px;background:var(--footer)}
.footer-links{left:83px;top:0;line-height:30px;font-size:7.5px;color:#fff;display:flex;gap:10px}
.footer-copy{left:552px;top:0;line-height:30px;font-size:7px;color:#fff}
.footer .social{left:700px;top:8px}
.footer .social span{width:14px;height:14px}
.footer .social span:first-child{background:#111}
.footer .social span:nth-child(n+2){background:#aaa}
</style>
</head>
<body>

<div class="abs top-bar"></div>
<div class="abs toll">TOLL FREE: <b>1800 4417 902</b></div>

<header class="abs nav">
  <div class="abs brand">TINDRAL</div>
  <nav class="abs menu">
    <a style="left:312px">HOME</a>
    <a class="active" style="left:350px">ABOUT US</a>
    <a style="left:425px">SERVICES</a>
    <a style="left:487px">PORTFOLIO</a>
    <a style="left:558px">OUR TEAM</a>
    <a style="left:624px">CONTACT US</a>
  </nav>
  <div class="abs social" style="left:700px"><span></span><span></span><span></span></div>
</header>

<section class="abs hero" role="img" aria-label="Photo of hands typing on a laptop showing a dashboard on a wooden desk"></section>
<h1 class="abs hero-title">Tindral a Software and<br>Development Company...</h1>
<div class="abs btn-cta">Call to Action</div>
<div class="abs learn" style="left:221px;top:285px">Learn More <i></i></div>
<div class="abs dots"><span></span><span></span><span></span></div>

<h2 class="abs section-title" style="left:0;width:826px;text-align:center;top:471px">Our Services</h2>
<div class="abs rule" style="left:238px;top:508px;width:352px"></div>
<div class="abs rule-bar" style="left:402px;top:506px;width:22px"></div>

<svg class="abs" style="left:155px;top:580px" width="94" height="58" viewBox="0 0 94 58">
  <rect x="11" y="3" width="71" height="48" fill="none" stroke="#222" stroke-width="3"/>
  <rect x="1" y="52" width="92" height="4" rx="1" fill="#222"/>
</svg>
<svg class="abs" style="left:396px;top:570px" width="34" height="68" viewBox="0 0 34 68">
  <rect x="2" y="1" width="30" height="66" rx="4" fill="#222"/>
  <rect x="6" y="7" width="22" height="54" fill="#fff"/>
</svg>
<svg class="abs" style="left:588px;top:576px" width="72" height="62" viewBox="0 0 72 62">
  <rect x="2" y="2" width="68" height="44" rx="3" fill="none" stroke="#222" stroke-width="4"/>
  <rect x="30" y="48" width="12" height="8" fill="#222"/>
  <path d="M18 60 Q36 52 54 60" fill="none" stroke="#222" stroke-width="3"/>
</svg>

<div class="abs svc" style="left:107px;top:654px">
  <h3>Web Application</h3>
  <p>Lorem ipsum dolor sit amet, consectetur adipisicing elit, sed do eiusmod tempor incididunt ut et dolore</p>
  <div class="learn">Learn More <i></i></div>
</div>
<div class="abs svc" style="left:318px;top:654px">
  <h3>App Application</h3>
  <p>Lorem ipsum dolor sit amet, consectetur adipisicing elit, sed do eiusmod tempor incididunt ut et dolore</p>
  <div class="learn">Learn More <i></i></div>
</div>
<div class="abs svc" style="left:529px;top:654px">
  <h3>Desktop Application</h3>
  <p>Lorem ipsum dolor sit amet, consectetur adipisicing elit, sed do eiusmod tempor incididunt ut et dolore</p>
  <div class="learn">Learn More <i></i></div>
</div>

<h3 class="abs col-title" style="left:82px;top:842px">About Us</h3>
<div class="abs rule" style="left:82px;top:868px;width:164px"></div>
<div class="abs rule-bar" style="left:82px;top:866px;width:23px"></div>
<div class="abs" style="left:82px;top:885px;width:166px;height:123px;background:linear-gradient(90deg,#e9e7e3,#f2f1ee)" role="img" aria-label="Promotional photo of a man in a white t-shirt leaning against a wall"></div>
<p class="abs about-text" style="left:82px;top:1018px;width:175px">Lorem ipsum dolor sit amet, consectetur adipisicing elit, sed do eiusmod tempor incididunt ut labore et dolore magna aliqua. Ut enim ad minim veniam, quis nostrud exercitation ullamco laboris nisi</p>
<div class="abs learn" style="left:187px;top:1097px">Learn More <i></i></div>

<h3 class="abs col-title" style="left:282px;top:842px">Contact Us</h3>
<div class="abs rule" style="left:282px;top:868px;width:165px"></div>
<div class="abs rule-bar" style="left:282px;top:866px;width:23px"></div>
<div class="abs" style="left:282px;top:885px;width:167px;height:192px;background:linear-gradient(135deg,#a9c8ee,#e7e4d6 55%,#a9c8ee)" role="img" aria-label="Road map of the office region"></div>
<div class="abs learn" style="left:371px;top:1097px">Enlarge Full Map <i></i></div>

<h3 class="abs col-title" style="left:479px;top:842px">Our Portfolio</h3>
<div class="abs rule" style="left:479px;top:868px;width:243px"></div>
<div class="abs rule-bar" style="left:479px;top:866px;width:23px"></div>

<div class="abs tile" style="left:481px;top:890px;background:linear-gradient(120deg,#3a3a44,#8a6a5a)" role="img" aria-label="Website preview with cycling theme">
  <div class="cap">Lorem Ipsum Text<i></i></div></div>
<div class="abs tile" style="left:606px;top:890px;background:linear-gradient(120deg,#2a2a2a,#7a7a7a)" role="img" aria-label="Website preview in black and white">
  <div class="cap">Lorem Ipsum Text<i></i></div></div>
<div class="abs tile" style="left:481px;top:1006px;background:linear-gradient(#f6e7a8,#c9e4a0)" role="img" aria-label="Colourful illustrated blog website preview">
  <div class="cap">Lorem Ipsum Text<i></i></div></div>
<div class="abs tile" style="left:606px;top:1006px;background:linear-gradient(#8fb8d8,#6a9a3a)" role="img" aria-label="Website preview of a country estate with lawn">
  <div class="cap">Lorem Ipsum Text<i></i></div></div>

<footer class="abs footer">
  <div class="abs footer-links"><span>HOME</span><span>ABOUT US</span><span>SERVICES</span><span>PORTFOLIO</span><span>OUR TEAM</span><span>CONTACT US</span></div>
  <div class="abs footer-copy">© Copyright 2014 &nbsp;·&nbsp; Terms and Conditions</div>
  <div class="abs social"><span></span><span></span><span></span></div>
</footer>

</body>
</html>
```